Tamworth Logistics

Create a modern, simple, Elegant business card design for my business.

Services: Vexa Trucks, Transport, Contract Logistics,

Business

Include all details same as old card plus new website address: www.tamworthlogistics-demo.com.au

• Similar colors to Logo.

```html
<!DOCTYPE html>
<html lang="en">
<head>
<meta charset="utf-8">
<title>Tamworth Logistics – Business Card</title>
<link href="https://fonts.googleapis.com/css2?family=Arimo:wght@400;600&display=swap" rel="stylesheet">
<style>
  :root {
    --page-bg: #e4e1dc;
    --card-frost: #f1f0ee;
    --card-frost-edge: #dcdde0;
    --blue-light: #2f76ad;
    --blue-deep: #123a5a;
    --swoosh-grey: #6b6c70;
    --brand-ink: #3e4650;
    --detail-ink: #d9cfbf;
    --icon-bg: #d3c9b8;
    --icon-ink: #1d4566;
  }
  * { margin: 0; padding: 0; box-sizing: border-box; }
  html, body { width: 1200px; height: 970px; overflow: hidden; }
  body {
    background: var(--page-bg);
    font-family: "Arimo", Arial, sans-serif;
    position: relative;
  }
  .business-card {
    position: absolute;
    left: 80px; top: 189px;
    width: 1040px; height: 592px;
    background: linear-gradient(160deg, var(--card-frost) 0%, var(--card-frost-edge) 100%);
    box-shadow: 0 14px 40px rgba(0,0,0,0.18);
    overflow: hidden;
  }
  .card-shapes { position: absolute; inset: 0; }
  .brand-name {
    position: absolute;
    left: 62px; top: 112px;
    font-size: 54px;
    font-weight: 600;
    color: var(--brand-ink);
    letter-spacing: 0.5px;
  }
  .holder {
    position: absolute;
    right: 35px; top: 338px;
    text-align: right;
    color: var(--detail-ink);
  }
  .holder-name { font-size: 33px; font-weight: 600; letter-spacing: 0.5px; line-height: 1.1; }
  .holder-role { font-size: 24px; font-weight: 400; line-height: 1.2; }
  .contact-list {
    position: absolute;
    right: 35px; top: 446px;
    list-style: none;
    color: var(--detail-ink);
    font-size: 24.5px;
  }
  .contact-item {
    display: flex; align-items: center; justify-content: flex-end;
    gap: 10px; height: 36px;
  }
  .contact-icon {
    width: 30px; height: 30px;
    background: var(--icon-bg);
    display: flex; align-items: center; justify-content: center;
  }
  .contact-icon svg { width: 22px; height: 22px; }
</style>
</head>
<body>
  <section class="business-card">
    <svg class="card-shapes" viewBox="0 0 1040 592" width="1040" height="592" aria-hidden="true">
      <defs>
        <linearGradient id="blueArea" x1="1" y1="0" x2="0.3" y2="1">
          <stop offset="0" stop-color="var(--blue-light)"/>
          <stop offset="1" stop-color="var(--blue-deep)"/>
        </linearGradient>
      </defs>
      <path d="M912,0 C810,250 520,520 190,592 L1040,592 L1040,0 Z" fill="url(#blueArea)"/>
      <path d="M884,38 C780,300 470,530 150,588 C480,515 760,300 884,38 Z" fill="var(--swoosh-grey)" stroke="var(--swoosh-grey)" stroke-width="3"/>
    </svg>

    <div class="brand-name">Tamworth Logistics</div>

    <div class="holder">
      <div class="holder-name">ALEX MORGAN</div>
      <div class="holder-role">Manager</div>
    </div>

    <ul class="contact-list">
      <li class="contact-item">
        <span>0400123987</span>
        <span class="contact-icon">
          <svg viewBox="0 0 24 24"><path d="M4 9c0-3 4-4 8-4s8 1 8 4v2h-4V9H8v2H4z" fill="var(--icon-ink)"/><rect x="6" y="12" width="12" height="8" rx="1" fill="var(--icon-ink)"/></svg>
        </span>
      </li>
      <li class="contact-item">
        <span>info@tamworthlogistics-demo.com.au</span>
        <span class="contact-icon">
          <svg viewBox="0 0 24 24"><rect x="3" y="6" width="18" height="12" fill="none" stroke="var(--icon-ink)" stroke-width="2"/><path d="M3 6l9 7 9-7" fill="none" stroke="var(--icon-ink)" stroke-width="2"/></svg>
        </span>
      </li>
      <li class="contact-item">
        <span>www.tamworthlogistics-demo.com.au</span>
        <span class="contact-icon">
          <svg viewBox="0 0 24 24" fill="none" stroke="var(--icon-ink)" stroke-width="1.6"><circle cx="12" cy="12" r="8.5"/><ellipse cx="12" cy="12" rx="4" ry="8.5"/><path d="M3.5 12h17M5 7.5h14M5 16.5h14"/></svg>
        </span>
      </li>
    </ul>
  </section>
</body>
</html>
```